Road Construction Company needs business cards

We would like a new business card designed for our business.

We're a road construction company based in Qld, Australia.

Can the business card please have the following information on it.

Name: Brent Malvoy
Position: General Manager
Phone: 0471 592 304
Email: Brent.malvoy@quendix.com.au
Address: 87 Harrowgate Ave, Pindarra, QLD, 4000
Website: www.quendix.com.au

Visually we'd like the card to be professional and simple.

Attached is our logo.

Our website is www.quendix.com.au

Target Market(s)

Men aged 25-60

Contact Information for Business Card

As listed in project description

Font styles to use
Serif

Requirements
Must have
• Large logo on back of card

```html
<!DOCTYPE html>
<html lang="en">
<head>
<meta charset="utf-8">
<title>Quendix Business Card</title>
<link href="https://fonts.googleapis.com/css2?family=Poppins:wght@400;700&display=swap" rel="stylesheet">
<style>
  :root {
    --stage: #979797;
    --card-dark: #231f20;
    --card-light: #ffffff;
    --brand-blue: #0b55a5;
    --accent-blue: #3ba2d9;
    --text-grey: #5f5f5f;
    --rule-grey: #9a9a9a;
    --divider: #555555;
  }
  * { margin: 0; padding: 0; box-sizing: border-box; }
  html, body { width: 1200px; height: 1000px; overflow: hidden; }
  body {
    background: var(--stage);
    position: relative;
    font-family: "Poppins", sans-serif;
  }
  .card {
    position: absolute;
    left: 293px;
    width: 615px;
    height: 351px;
    border-radius: 34px;
    overflow: hidden;
  }
  .card--front { top: 121px; background: var(--card-dark); }
  .card--back { top: 533px; background: var(--card-light); }

  .front-decoration {
    position: absolute;
    top: 0;
    right: 0;
    width: 380px;
    height: 351px;
    background: linear-gradient(115deg, rgba(35, 31, 32, 0) 35%, rgba(30, 95, 169, 0.16) 70%, rgba(46, 166, 220, 0.24) 100%);
  }

  .brand {
    position: absolute;
    left: 0; right: 0;
    text-align: center;
    line-height: 1;
  }
  .brand--front { top: 141px; }
  .brand--back { top: 42px; }
  .brand__name {
    font-weight: 700;
    letter-spacing: 3px;
  }
  .brand--front .brand__name { font-size: 50px; color: #ffffff; }
  .brand--back .brand__name { font-size: 44px; color: var(--brand-blue); }
  .brand__tagline {
    font-weight: 700;
    color: var(--accent-blue);
    text-transform: uppercase;
  }
  .brand--front .brand__tagline { font-size: 12px; letter-spacing: 5.5px; margin-top: 4px; }
  .brand--back .brand__tagline { font-size: 10px; letter-spacing: 4.6px; margin-top: 2px; }

  .person {
    position: absolute;
    right: 327px;
    top: 178px;
    text-align: right;
  }
  .person__name {
    font-size: 17px;
    font-weight: 700;
    color: var(--brand-blue);
    letter-spacing: 0.5px;
    text-transform: uppercase;
    line-height: 22px;
  }
  .person__role {
    font-size: 14px;
    color: var(--accent-blue);
    line-height: 18px;
  }
  .divider {
    position: absolute;
    left: 307px;
    top: 160px;
    width: 1px;
    height: 81px;
    background: var(--divider);
  }
  .contacts {
    position: absolute;
    left: 324px;
    top: 170px;
    list-style: none;
  }
  .contacts li {
    display: flex;
    align-items: center;
    height: 21px;
    font-size: 14px;
    color: var(--text-grey);
  }
  .contacts svg { width: 15px; height: 15px; margin-right: 8px; flex: none; }
  .address-rule {
    position: absolute;
    left: 26px;
    right: 26px;
    top: 306px;
    height: 1px;
    background: var(--rule-grey);
  }
  .address {
    position: absolute;
    left: 0; right: 0;
    top: 317px;
    text-align: center;
    font-size: 13.5px;
    color: var(--text-grey);
  }
</style>
</head>
<body>
  <section class="card card--front">
    <div class="front-decoration" role="img" aria-label="Decorative blue line pattern suggesting a road rising to a peak"></div>
    <div class="brand brand--front">
      <div class="brand__name">QUENDIX</div>
      <div class="brand__tagline">Road Construction</div>
    </div>
  </section>

  <section class="card card--back">
    <div class="brand brand--back">
      <div class="brand__name">QUENDIX</div>
      <div class="brand__tagline">Road Construction</div>
    </div>

    <div class="person">
      <div class="person__name">Brent Malvoy</div>
      <div class="person__role">General Manager</div>
    </div>

    <div class="divider"></div>

    <ul class="contacts">
      <li>
        <svg viewBox="0 0 24 24" fill="var(--accent-blue)"><path d="M6.6 10.8a15.1 15.1 0 0 0 6.6 6.6l2.2-2.2c.3-.3.7-.4 1-.2 1.1.4 2.3.6 3.6.6.6 0 1 .4 1 1V20c0 .6-.4 1-1 1A17 17 0 0 1 3 4c0-.6.4-1 1-1h3.5c.6 0 1 .4 1 1 0 1.3.2 2.5.6 3.6.1.3 0 .7-.2 1z"/></svg>
        0471 592 304
      </li>
      <li>
        <svg viewBox="0 0 24 24" fill="var(--accent-blue)"><path d="M2 5h20v14H2z"/><path d="M2 5l10 8 10-8" stroke="#fff" stroke-width="1.6" fill="none"/></svg>
        brent.malvoy@quendix.com.au
      </li>
      <li>
        <svg viewBox="0 0 24 24" fill="none" stroke="var(--accent-blue)" stroke-width="2"><circle cx="12" cy="12" r="9"/><path d="M3 12h18M12 3c3 3 3 15 0 18M12 3c-3 3-3 15 0 18"/></svg>
        www.quendix.com.au
      </li>
    </ul>

    <div class="address-rule"></div>
    <p class="address">87 Harrowgate Ave, Pindarra, QLD, 4000</p>
  </section>
</body>
</html>
```